Coffeeshop menu for filter tip

We want to have a cannabis (coffeeshop) menu in the size 25mm wide x 60mm wide. Some examples attached.

it must have the following text:
Menu

WEED p/g
Velotrine €16
Cinderfox €14
Tide Rambler €14
Marigolden €16
Grand Pelican €14
Copper Comet €14

HASH p/g
Baltic Ember €12
Harbor Velvet€11
Plum Rova €14
Dusk Maple €10

Target Market(s)

tourist in Amsterdam

Requirements
Nice to have
• cannabis sign leaf
• No Cigarettes allowed symbol

```html
<!DOCTYPE html>
<html lang="en">
<head>
<meta charset="utf-8">
<title>Coffeeshop Menu</title>
<link href="https://fonts.googleapis.com/css2?family=Bree+Serif&family=Stint+Ultra+Expanded&display=swap" rel="stylesheet">
<style>
  :root {
    --page: #ffffff;
    --card: #000000;
    --leaf-green: #2b4f17;
    --leaf-brown: #5a2d05;
    --weed-green: #4a9a40;
    --hash-olive: #9ca43e;
    --white: #ffffff;
    --sign-red: #e3202a;
  }
  * { margin: 0; padding: 0; box-sizing: border-box; }
  html, body { width: 1200px; height: 1200px; overflow: hidden; background: var(--page); }
  .menu-card {
    position: absolute; left: 372px; top: 80px; width: 443px; height: 1065px;
    background: var(--card); overflow: hidden;
    box-shadow: 0 14px 18px -10px rgba(0,0,0,0.25);
    font-family: "Bree Serif", Georgia, serif; color: var(--white);
  }
  .foliage-backdrop {
    position: absolute; inset: 0;
    background: linear-gradient(180deg,
      var(--leaf-green) 0%, rgba(43,79,23,0.85) 25%, rgba(35,37,58,0.7) 45%,
      rgba(35,37,58,0.55) 62%, rgba(90,45,5,0.55) 80%, var(--leaf-brown) 100%);
    opacity: 0.75;
  }
  .menu-emblem { position: absolute; left: 75px; top: 31px; width: 294px; height: 201px; }
  .emblem-art {
    position: absolute; inset: 0; border-radius: 24px;
    background: radial-gradient(ellipse at 50% 40%, #8a82c0 0%, #b86a6a 45%, #7a3a2a 80%, rgba(43,79,23,0) 100%);
    opacity: 0.8;
  }
  .emblem-title {
    position: absolute; left: 0; right: 0; top: 150px; text-align: center;
    font-size: 44px; font-weight: 400; line-height: 1; color: var(--white);
  }
  .section-pill {
    position: absolute; left: 20px; width: 397px; height: 65px; border-radius: 33px; overflow: hidden;
    display: flex; align-items: center;
  }
  .section-pill .label {
    height: 100%; width: 257px; background: var(--white); border-radius: 33px;
    display: flex; align-items: center; padding-left: 26px;
    font-family: "Stint Ultra Expanded", "Courier New", serif; font-size: 33px; font-weight: 700;
  }
  .section-pill .unit {
    flex: 1; text-align: center; font-family: "Stint Ultra Expanded", "Courier New", serif;
    font-size: 33px; font-weight: 700; color: var(--white);
  }
  .pill-weed { top: 285px; background: var(--weed-green); }
  .pill-weed .label { color: var(--weed-green); }
  .pill-hash { top: 660px; background: var(--hash-olive); }
  .pill-hash .label { color: var(--hash-olive); }
  .price-list { position: absolute; left: 37px; right: 60px; list-style: none; }
  .price-list li { display: flex; justify-content: space-between; font-size: 38px; line-height: 44px; }
  .list-weed { top: 357px; }
  .list-hash { top: 735px; }
  .house-signs { position: absolute; left: 35px; top: 952px; display: flex; gap: 26px; }
  .house-signs svg { width: 86px; height: 86px; }
</style>
</head>
<body>
  <main class="menu-card">
    <div class="foliage-backdrop" role="img" aria-label="Dark silhouettes of cannabis plants in green, blue and brown tones"></div>

    <header class="menu-emblem">
      <div class="emblem-art" role="img" aria-label="Rainbow sunburst badge with a cannabis leaf above a ribbon banner"></div>
      <h1 class="emblem-title">Menu</h1>
    </header>

    <div class="section-pill pill-weed"><span class="label">WEED</span><span class="unit">p/g</span></div>
    <ul class="price-list list-weed">
      <li><span>Velotrine</span><span>€16</span></li>
      <li><span>Cinderfox</span><span>€14</span></li>
      <li><span>Tide Rambler</span><span>€14</span></li>
      <li><span>Marigolden</span><span>€16</span></li>
      <li><span>Grand Pelican</span><span>€14</span></li>
      <li><span>Copper Comet</span><span>€14</span></li>
    </ul>

    <div class="section-pill pill-hash"><span class="label">HASH</span><span class="unit">p/g</span></div>
    <ul class="price-list list-hash">
      <li><span>Baltic Ember</span><span>€12</span></li>
      <li><span>Harbor Velvet</span><span>€11</span></li>
      <li><span>Plum Rova</span><span>€14</span></li>
      <li><span>Dusk Maple</span><span>€10</span></li>
    </ul>

    <footer class="house-signs">
      <svg viewBox="0 0 84 84" role="img" aria-label="No cigarettes allowed">
        <circle cx="42" cy="42" r="37" fill="var(--white)" stroke="var(--sign-red)" stroke-width="9"/>
        <rect x="16" y="41" width="44" height="8" fill="#000"/>
        <rect x="61" y="41" width="3" height="8" fill="#000"/>
        <rect x="66" y="41" width="3" height="8" fill="#000"/>
        <path d="M58 36 q-6 -8 0 -16 M64 36 q-6 -8 0 -16" fill="none" stroke="#000" stroke-width="2.5"/>
        <line x1="16" y1="16" x2="68" y2="68" stroke="var(--sign-red)" stroke-width="9"/>
      </svg>
      <svg viewBox="0 0 84 84" role="img" aria-label="Cannabis allowed badge">
        <circle cx="42" cy="42" r="37" fill="var(--white)" stroke="var(--weed-green)" stroke-width="9"/>
        <circle cx="42" cy="42" r="22" fill="var(--weed-green)" opacity="0.85"/>
      </svg>
    </footer>
  </main>
</body>
</html>
```